Corporate Business Card

Very professional, Modern, Not to busy, include phone address email, website
(253) 555-0174, 61807 19th Street N, Kent, WA 98517, marcus@kestrelbayholding.com, brelvanindustries.com

Target Market(s)

Manufacturing

Industry/Entity Type

Aero, machining, manufacturing, Off road racing

Contact Information for Business Card

Phone, address email, website

```html
<!DOCTYPE html>
<html lang="en">
<head>
<meta charset="utf-8">
<title>Brelvan Industries – Business Card</title>
<link rel="stylesheet" href="https://fonts.googleapis.com/css2?family=Saira:wght@400;500;700&display=swap">
<style>
  :root {
    --canvas: #ebecec;
    --navy: #2c4a7e;
    --navy-deep: #233f70;
    --ink: #2d4373;
    --red: #e8393b;
    --white: #ffffff;
    --muted: #4a4f5a;
  }
  * { box-sizing: border-box; margin: 0; padding: 0; }
  html, body {
    width: 1200px; height: 800px; overflow: hidden;
    background: var(--canvas);
    font-family: "Saira", sans-serif;
  }
  .sheet {
    position: relative; width: 1200px; height: 800px;
    display: flex; align-items: center; justify-content: center; gap: 60px;
  }
  .card {
    position: relative; width: 500px; height: 286px;
    box-shadow: 0 10px 30px rgba(0,0,0,0.12);
  }
  /* Front */
  .card--front {
    background: linear-gradient(120deg, var(--navy) 0%, var(--navy-deep) 100%);
    display: flex; align-items: center; justify-content: center;
  }
  .wordmark {
    font-weight: 700; color: var(--white);
    text-align: left; line-height: 1;
  }
  .wordmark__name { display: block; font-size: 54px; letter-spacing: 2px; }
  .wordmark__sub { display: block; font-size: 21px; letter-spacing: 3px; margin-top: 6px; text-align: right; }
  /* Back */
  .card--back { background: var(--white); }
  .card--back .wordmark {
    position: absolute; left: 38px; top: 36px; color: var(--ink);
  }
  .card--back .wordmark__name { font-size: 26px; letter-spacing: 1px; }
  .card--back .wordmark__sub { font-size: 10px; letter-spacing: 1.5px; margin-top: 3px; }
  .contact-list {
    list-style: none; position: absolute; left: 250px; top: 118px;
    display: flex; flex-direction: column; gap: 9px;
  }
  .contact-list__item {
    display: flex; align-items: center; gap: 9px;
    font-size: 13px; font-weight: 500; color: var(--ink);
  }
  .contact-list__icon { width: 12px; height: 12px; flex: none; }
  .address {
    position: absolute; left: 38px; bottom: 34px;
    font-size: 11px; font-weight: 500; color: var(--muted); letter-spacing: 0.3px;
  }
</style>
</head>
<body>
<main class="sheet">
  <section class="card card--front" aria-label="Card front">
    <div class="wordmark">
      <span class="wordmark__name">BRELVAN</span>
      <span class="wordmark__sub">Industries</span>
    </div>
  </section>

  <section class="card card--back" aria-label="Card back">
    <div class="wordmark">
      <span class="wordmark__name">BRELVAN</span>
      <span class="wordmark__sub">Industries</span>
    </div>

    <ul class="contact-list">
      <li class="contact-list__item">
        <svg class="contact-list__icon" viewBox="0 0 24 24" fill="var(--red)"><path d="M6.6 10.8c1.4 2.8 3.8 5.2 6.6 6.6l2.2-2.2c.3-.3.7-.4 1-.2 1.1.4 2.3.6 3.6.6.6 0 1 .4 1 1V20c0 .6-.4 1-1 1C10.6 21 3 13.4 3 4c0-.6.4-1 1-1h3.5c.6 0 1 .4 1 1 0 1.3.2 2.5.6 3.6.1.3 0 .7-.2 1z"/></svg>
        (253) 555-0174
      </li>
      <li class="contact-list__item">
        <svg class="contact-list__icon" viewBox="0 0 24 24" fill="var(--red)"><path d="M3 5h18v14H3z" opacity="0"/><path d="M20 4H4a2 2 0 0 0-2 2v12a2 2 0 0 0 2 2h16a2 2 0 0 0 2-2V6a2 2 0 0 0-2-2zm0 4-8 5-8-5V6l8 5 8-5z"/></svg>
        marcus@kestrelbayholding.com
      </li>
      <li class="contact-list__item">
        <svg class="contact-list__icon" viewBox="0 0 24 24" fill="none" stroke="var(--red)" stroke-width="2.4"><circle cx="12" cy="12" r="9"/><path d="M3 12h18M12 3c3 3 3 15 0 18M12 3c-3 3-3 15 0 18"/></svg>
        brelvanindustries.com
      </li>
    </ul>

    <p class="address">61807 19th Street N, Kent, WA 98517</p>
  </section>
</main>
</body>
</html>
```